Cedar Hall businesscard

We changed our name and logo, now we need new business cards.
3-4/72 Marlow Street Blacktown 2148
www.cedarhall-example.org.au
info@cedarhall-example.org.au
Lorna-Jean Whitcombe
Senior Pastor
ph: 02 95874210

```html
<!DOCTYPE html>
<html lang="en">
<head>
<meta charset="utf-8">
<title>Cedar Hall — Business Card</title>
<link rel="stylesheet" href="https://fonts.googleapis.com/css2?family=Michroma&display=swap">
<style>
  :root {
    --backdrop: #e4e6e8;
    --card-white: #f7f8f9;
    --card-sheen: #e3e6e9;
    --slate: #8593a0;
    --slate-deep: #7a8896;
    --stripe: #c7ced5;
    --ink-light: #ffffff;
    --card-shadow: rgba(40, 50, 60, 0.22);
  }
  * { margin: 0; padding: 0; box-sizing: border-box; }
  html, body {
    width: 1200px;
    height: 899px;
    overflow: hidden;
    background: var(--backdrop);
  }
  .canvas {
    position: relative;
    width: 1200px;
    height: 899px;
  }
  .business-card {
    position: absolute;
    left: 150px;
    top: 192px;
    width: 900px;
    height: 514px;
    border-radius: 46px;
    overflow: hidden;
    box-shadow: 0 18px 40px var(--card-shadow);
    font-family: "Michroma", "Arial", sans-serif;
    color: var(--ink-light);
  }
  .card-art {
    position: absolute;
    inset: 0;
    width: 900px;
    height: 514px;
  }
  .logo-mark {
    position: absolute;
    left: 370px;
    top: 34px;
    width: 160px;
    height: 160px;
    border-radius: 50%;
    background: var(--slate);
    display: flex;
    align-items: center;
    justify-content: center;
  }
  .logo-name {
    font-size: 21px;
    line-height: 1.15;
    letter-spacing: 2px;
    text-align: center;
    color: var(--ink-light);
  }
  .holder {
    position: absolute;
    right: 490px;
    top: 336px;
    text-align: right;
    white-space: nowrap;
  }
  .holder-name {
    font-size: 17px;
    letter-spacing: 1.5px;
    margin-bottom: 6px;
  }
  .holder-role {
    font-size: 13px;
    letter-spacing: 1.5px;
    margin-bottom: 18px;
  }
  .holder-address {
    font-size: 13px;
    letter-spacing: 1.5px;
    line-height: 1.9;
  }
  .divider {
    position: absolute;
    left: 428px;
    top: 338px;
    width: 2px;
    height: 124px;
    background: var(--ink-light);
    opacity: 0.85;
  }
  .contact-list {
    position: absolute;
    left: 446px;
    top: 340px;
    list-style: none;
    white-space: nowrap;
  }
  .contact-item {
    display: flex;
    align-items: center;
    gap: 10px;
    height: 30px;
    font-size: 13px;
    letter-spacing: 1.2px;
  }
  .contact-icon {
    width: 20px;
    height: 20px;
    flex: none;
  }
</style>
</head>
<body>
<main class="canvas">
  <section class="business-card" aria-label="Cedar Hall business card">
    <svg class="card-art" viewBox="0 0 900 514" aria-hidden="true">
      <defs>
        <linearGradient id="card-face" x1="0" y1="0" x2="1" y2="1">
          <stop offset="0" stop-color="var(--card-white)"/>
          <stop offset="0.55" stop-color="var(--card-sheen)"/>
          <stop offset="1" stop-color="var(--card-white)"/>
        </linearGradient>
      </defs>
      <rect class="card-face" width="900" height="514" fill="url(#card-face)"/>
      <path class="wave-stripe" d="M0 200 C 200 226, 360 290, 540 286 C 700 282, 800 236, 900 230 L900 514 L0 514 Z" fill="var(--stripe)"/>
      <path class="wave-gap" d="M0 210 C 200 238, 360 302, 540 298 C 700 294, 800 250, 900 244 L900 514 L0 514 Z" fill="var(--card-white)"/>
      <path class="wave-band" d="M0 222 C 200 252, 360 316, 540 312 C 700 308, 800 266, 900 260 L900 514 L0 514 Z" fill="var(--slate)"/>
    </svg>

    <div class="logo-mark">
      <span class="logo-name">CEDAR<br>HALL</span>
    </div>

    <div class="holder">
      <p class="holder-name">Lorna-Jean Whitcombe</p>
      <p class="holder-role">Senior Pastor</p>
      <p class="holder-address">3-4/72 Marlow Street<br>Blacktown 2148</p>
    </div>

    <div class="divider"></div>

    <ul class="contact-list">
      <li class="contact-item">
        <svg class="contact-icon" viewBox="0 0 20 20" aria-hidden="true"><circle cx="10" cy="10" r="10" fill="#fff"/><path d="M6.5 5.5 L8.5 5.5 L9.3 8 L8 9 Q9 11.2 11 12 L12 10.7 L14.5 11.5 L14.5 13.5 Q9 14.5 6.5 8 Z" fill="var(--slate-deep)"/></svg>
        <span>ph: 02 95874210</span>
      </li>
      <li class="contact-item">
        <svg class="contact-icon" viewBox="0 0 20 20" aria-hidden="true"><circle cx="10" cy="10" r="10" fill="#fff"/><rect x="5" y="6.5" width="10" height="7" fill="var(--slate-deep)"/><path d="M5 6.5 L10 10.5 L15 6.5" fill="none" stroke="#fff" stroke-width="1"/></svg>
        <span>info@cedarhall-example.org.au</span>
      </li>
      <li class="contact-item">
        <svg class="contact-icon" viewBox="0 0 20 20" aria-hidden="true"><circle cx="10" cy="10" r="10" fill="#fff"/><circle cx="10" cy="10" r="5" fill="none" stroke="var(--slate-deep)" stroke-width="1.3"/><path d="M5 10 H15 M10 5 Q7 10 10 15 M10 5 Q13 10 10 15" fill="none" stroke="var(--slate-deep)" stroke-width="1"/></svg>
        <span>www.cedarhall-example.org.au</span>
      </li>
    </ul>
  </section>
</main>
</body>
</html>
```